iOS App Design - Google Material Design + Signal

What we would love to do is to create an activity feed page plus main navigation for our iOS application. If we like this design then we'd like to hire someone to take the design elements and build out the rest of our screens.

The design must use Google Material Design and be delivered in a Signal file.

Our product is an application for activity provider owners to manage their daily business while on the go. This activity feed/home screen will provide them with information about their bookings, tours that day, etc.

We would like for it to be modern and eye catching, yet simple and functional for someone to use outdoors and while not in an office.

For this home screen, the main elements we would like to include:

- Main App Navigation with 4 elements: Home, Availability/Calendar, Booking and Settings
- A way to add a booking (plus sign or similar that is a constant - nav or floating

- A couple of overall key metrics that indicate how you the user’s business is doing that month that are static - not part of the feed

- A way to show different types of activity in a "news feed" - i.e. if a booking has happened or there is an upcoming tour, if a payment has been made to your account, suggestion on how to improve your profile.

- A way to filter the activities

We are open to the layout and options for these main elements above, we would like your opinion on how best from a user design perspective we can implement these.

Please let us know if you have any questions.

```html
<!DOCTYPE html>
<html lang="en">
<head>
<meta charset="utf-8">
<title>Your Bookings</title>
<link rel="stylesheet" href="https://fonts.googleapis.com/css2?family=Roboto:wght@400;500;700&display=swap">
<style>
:root{
  --blue-dark:#1f73c4;
  --blue-light:#3fb6ea;
  --accent:#1a8fd8;
  --ink:#1c1c1c;
  --muted:#6f6f6f;
  --bg:#eef1f5;
  --card:#ffffff;
  --line:#e1e5ea;
  --booking:#2b8fd5;
  --tour:#1b6aa5;
  --payment:#45bbe8;
  --fab:#f28a1a;
  --nav-idle:#8b8b8b;
}
*{box-sizing:border-box;margin:0;padding:0}
html,body{width:675px;height:1200px;overflow:hidden}
body{font-family:"Roboto",Arial,sans-serif;background:var(--bg);position:relative;color:var(--ink)}
.app-header{position:absolute;left:0;top:0;width:675px;height:122px;background:linear-gradient(90deg,var(--blue-dark),var(--blue-light));color:#fff}
.status-bar{position:absolute;top:0;left:0;right:0;height:36px;font-size:22px;font-weight:500}
.status-bar .carrier{position:absolute;left:10px;top:6px;display:flex;align-items:center;gap:8px}
.status-bar .time{position:absolute;left:0;right:0;top:6px;text-align:center}
.status-bar .battery{position:absolute;right:10px;top:6px;display:flex;align-items:center;gap:8px}
.app-title{position:absolute;left:22px;top:58px;font-size:29px;font-weight:500}
.search-btn{position:absolute;right:18px;top:54px}
.stats-card{position:absolute;left:14px;top:137px;width:647px;height:263px;background:var(--card);border-radius:4px;box-shadow:0 1px 3px rgba(0,0,0,.08)}
.stats-divider{position:absolute;left:326px;top:0;bottom:0;width:1px;background:var(--line)}
.stat{position:absolute;top:0;height:263px;text-align:center}
.stat-slots{left:0;width:326px}
.stat-revenue{left:327px;width:320px}
.ring{position:absolute;left:82px;top:24px}
.ring-value{position:absolute;left:0;right:0;top:76px;font-size:33px;color:var(--accent);font-weight:500}
.ring-label{position:absolute;left:0;right:0;top:116px;font-size:16px;line-height:19px;color:#333}
.stat-caption{position:absolute;left:0;right:0;top:202px;font-size:22px;color:#222}
.wave{position:absolute;left:136px;top:62px}
.revenue-value{position:absolute;left:0;right:0;top:100px;font-size:44px;color:var(--accent);font-weight:400}
.revenue-caption{position:absolute;left:0;right:0;top:170px;font-size:21px;line-height:23px;color:#222}
.feed-filter{position:absolute;left:0;right:0;top:426px;text-align:center;font-size:22px;font-weight:500;letter-spacing:2px;color:#333}
.feed-filter svg{vertical-align:middle;margin-left:4px}
.timeline-line{position:absolute;left:57px;top:520px;width:2px;height:600px;background:#c9d2dc}
.feed-item{position:absolute;left:112px;width:543px;background:var(--card);border-radius:4px;box-shadow:0 1px 2px rgba(0,0,0,.06);padding:18px 0 0 44px}
.feed-type{font-size:15px;letter-spacing:1.6px;color:var(--muted);font-weight:500}
.feed-title{font-size:26px;font-weight:500;margin-top:8px;color:var(--ink)}
.feed-meta{display:flex;gap:28px;margin-top:12px;font-size:20px;color:#222}
.feed-meta span{display:flex;align-items:center;gap:6px}
.feed-dot{position:absolute;left:20px;width:76px;height:76px;border-radius:50%;display:flex;align-items:center;justify-content:center}
.dot-booking{background:var(--booking)}
.dot-tour{background:var(--tour)}
.dot-payment{background:var(--payment)}
.fab{position:absolute;left:546px;top:990px;width:100px;height:100px;border-radius:50%;background:var(--fab);box-shadow:0 3px 8px rgba(0,0,0,.25);display:flex;align-items:center;justify-content:center}
.bottom-nav{position:absolute;left:0;top:1120px;width:675px;height:80px;background:#fff;border-top:1px solid var(--line);display:flex}
.nav-item{flex:1;text-align:center;padding-top:10px;font-size:17px;color:var(--nav-idle)}
.nav-item svg{display:block;margin:0 auto 4px}
.nav-item.active{color:var(--accent)}
.nav-badge{position:relative;display:inline-block}
.nav-badge::after{content:"";position:absolute;right:-4px;top:-2px;width:11px;height:11px;border-radius:50%;background:var(--fab)}
</style>
</head>
<body>
<header class="app-header">
  <div class="status-bar">
    <div class="carrier">
      <svg width="36" height="12" viewBox="0 0 36 12"><g fill="#fff"><circle cx="4" cy="6" r="3.5"/><circle cx="12" cy="6" r="3.5"/><circle cx="20" cy="6" r="3.5"/><circle cx="28" cy="6" r="3.5" fill-opacity=".5"/></g></svg>
      <span>Signal</span>
      <svg width="24" height="18" viewBox="0 0 24 18"><path d="M12 17l3-3.6a4.6 4.6 0 0 0-6 0zM5.5 9.6l2 2.3a7 7 0 0 1 9 0l2-2.3a10 10 0 0 0-13 0zM1.5 5l2 2.3a13.2 13.2 0 0 1 17 0l2-2.3a16.4 16.4 0 0 0-21 0z" fill="#fff"/></svg>
    </div>
    <div class="time">9:41 AM</div>
    <div class="battery">
      <svg width="12" height="20" viewBox="0 0 12 20"><path d="M1 5l10 9-5 4V2l5 4-10 9" fill="none" stroke="#fff" stroke-width="1.8"/></svg>
      <span>100%</span>
      <svg width="44" height="20" viewBox="0 0 44 20"><rect x="1" y="1" width="38" height="18" rx="4" fill="none" stroke="#fff" stroke-width="1.5"/><rect x="4" y="4" width="32" height="12" rx="2" fill="#fff"/><rect x="40.5" y="7" width="2.5" height="6" rx="1" fill="#fff"/></svg>
    </div>
  </div>
  <h1 class="app-title">Your Bookings</h1>
  <svg class="search-btn" width="38" height="38" viewBox="0 0 38 38"><circle cx="22" cy="15" r="11" fill="none" stroke="#fff" stroke-width="3"/><path d="M14 23L4 33" stroke="#fff" stroke-width="3.5" stroke-linecap="round"/></svg>
</header>

<section class="stats-card">
  <div class="stat stat-slots">
    <svg class="ring" width="162" height="162" viewBox="0 0 162 162">
      <circle cx="81" cy="81" r="72" fill="none" stroke="#ececec" stroke-width="10"/>
      <circle cx="81" cy="81" r="72" fill="none" stroke="#1aa7e0" stroke-width="10" stroke-dasharray="302 452" transform="rotate(-90 81 81)"/>
      <circle cx="81" cy="81" r="60" fill="#efefef"/>
    </svg>
    <div class="ring-value">8/12</div>
    <div class="ring-label">Slots<br>Available</div>
    <div class="stat-caption">Pending Availability</div>
  </div>
  <div class="stats-divider"></div>
  <div class="stat stat-revenue">
    <svg class="wave" width="48" height="30" viewBox="0 0 48 30"><g fill="none" stroke="#1a8fd8" stroke-width="2.6" stroke-linejoin="round"><path d="M2 12l8-9 8 8 10-8 8 7 10-8"/><path d="M2 26l8-9 8 8 10-8 8 7 10-8"/></g></svg>
    <div class="revenue-value">£354.60</div>
    <div class="revenue-caption">Revenue Earned<br>Yesterday</div>
  </div>
</section>

<div class="feed-filter">UPCOMING<svg width="20" height="12" viewBox="0 0 20 12"><path d="M2 2l8 8 8-8" fill="none" stroke="#333" stroke-width="2.5"/></svg></div>

<div class="timeline-line"></div>

<article class="feed-item" style="top:477px;height:131px">
  <div class="feed-type">UPCOMING BOOKING</div>
  <div class="feed-title">Booking with Rory Blake</div>
  <div class="feed-meta">
    <span><svg width="20" height="20" viewBox="0 0 20 20"><circle cx="10" cy="10" r="8" fill="none" stroke="#1a8fd8" stroke-width="2"/><path d="M10 5v5h4" fill="none" stroke="#1a8fd8" stroke-width="2"/></svg>13:30pm</span>
    <span><svg width="16" height="22" viewBox="0 0 16 22"><path d="M8 20S2 12.5 2 8a6 6 0 0 1 12 0c0 4.5-6 12-6 12z" fill="none" stroke="#1a8fd8" stroke-width="2"/><circle cx="8" cy="8" r="2" fill="#1a8fd8"/></svg>Edinburgh</span>
  </div>
</article>
<article class="feed-item" style="top:621px;height:128px">
  <div class="feed-type">UPCOMING TOUR</div>
  <div class="feed-title">Tour with Rory Blake</div>
  <div class="feed-meta">
    <span><svg width="20" height="20" viewBox="0 0 20 20"><circle cx="10" cy="10" r="8" fill="none" stroke="#1a8fd8" stroke-width="2"/><path d="M10 5v5h4" fill="none" stroke="#1a8fd8" stroke-width="2"/></svg>13:30pm</span>
    <span><svg width="16" height="22" viewBox="0 0 16 22"><path d="M8 20S2 12.5 2 8a6 6 0 0 1 12 0c0 4.5-6 12-6 12z" fill="none" stroke="#1a8fd8" stroke-width="2"/><circle cx="8" cy="8" r="2" fill="#1a8fd8"/></svg>Edinburgh</span>
  </div>
</article>
<article class="feed-item" style="top:761px;height:90px">
  <div class="feed-type">PAYMENT RECIEVED</div>
  <div class="feed-title">$45.50 recieved from Rory Blake</div>
</article>
<article class="feed-item" style="top:866px;height:128px">
  <div class="feed-type">UPCOMING BOOKING</div>
  <div class="feed-title">Booking with Rory Blake</div>
  <div class="feed-meta">
    <span><svg width="20" height="20" viewBox="0 0 20 20"><circle cx="10" cy="10" r="8" fill="none" stroke="#1a8fd8" stroke-width="2"/><path d="M10 5v5h4" fill="none" stroke="#1a8fd8" stroke-width="2"/></svg>13:30pm</span>
    <span><svg width="16" height="22" viewBox="0 0 16 22"><path d="M8 20S2 12.5 2 8a6 6 0 0 1 12 0c0 4.5-6 12-6 12z" fill="none" stroke="#1a8fd8" stroke-width="2"/><circle cx="8" cy="8" r="2" fill="#1a8fd8"/></svg>Edinburgh</span>
  </div>
</article>
<article class="feed-item" style="top:1008px;height:128px">
  <div class="feed-type">UPCOMING TOUR</div>
  <div class="feed-title">Tour with Rory Blake</div>
  <div class="feed-meta">
    <span><svg width="20" height="20" viewBox="0 0 20 20"><circle cx="10" cy="10" r="8" fill="none" stroke="#1a8fd8" stroke-width="2"/><path d="M10 5v5h4" fill="none" stroke="#1a8fd8" stroke-width="2"/></svg>13:30pm</span>
    <span><svg width="16" height="22" viewBox="0 0 16 22"><path d="M8 20S2 12.5 2 8a6 6 0 0 1 12 0c0 4.5-6 12-6 12z" fill="none" stroke="#1a8fd8" stroke-width="2"/><circle cx="8" cy="8" r="2" fill="#1a8fd8"/></svg>Edinburgh</span>
  </div>
</article>

<div class="feed-dot dot-booking" style="top:509px"><svg width="26" height="30" viewBox="0 0 26 30"><rect x="3" y="2" width="20" height="26" rx="2" fill="none" stroke="#fff" stroke-width="2.4"/><path d="M8 2v26M12 9h7" stroke="#fff" stroke-width="2.2"/></svg></div>
<div class="feed-dot dot-tour" style="top:651px"><svg width="24" height="32" viewBox="0 0 24 32"><path d="M12 29S3 18 3 11a9 9 0 0 1 18 0c0 7-9 18-9 18z" fill="none" stroke="#fff" stroke-width="2.4"/><circle cx="12" cy="11" r="3" fill="#fff"/></svg></div>
<div class="feed-dot dot-payment" style="top:768px"><svg width="32" height="28" viewBox="0 0 32 28"><path d="M6 12a10 9 0 0 1 19-3h3v7l-3 1-2 4v4h-4v-3h-6v3H9v-5a9 9 0 0 1-3-5H3v-4z" fill="none" stroke="#fff" stroke-width="2.2" stroke-linejoin="round"/><path d="M12 7h6" stroke="#fff" stroke-width="2.2"/></svg></div>
<div class="feed-dot dot-booking" style="top:896px"><svg width="26" height="30" viewBox="0 0 26 30"><rect x="3" y="2" width="20" height="26" rx="2" fill="none" stroke="#fff" stroke-width="2.4"/><path d="M8 2v26M12 9h7" stroke="#fff" stroke-width="2.2"/></svg></div>
<div class="feed-dot dot-tour" style="top:1035px"><svg width="24" height="32" viewBox="0 0 24 32"><path d="M12 29S3 18 3 11a9 9 0 0 1 18 0c0 7-9 18-9 18z" fill="none" stroke="#fff" stroke-width="2.4"/><circle cx="12" cy="11" r="3" fill="#fff"/></svg></div>

<div class="fab" aria-label="Add booking"><svg width="36" height="36" viewBox="0 0 36 36"><path d="M18 4v28M4 18h28" stroke="#fff" stroke-width="4.5" stroke-linecap="round"/></svg></div>

<nav class="bottom-nav">
  <div class="nav-item active"><svg width="34" height="32" viewBox="0 0 34 32"><path d="M3 15L17 3l14 12M7 12v17h8v-9h4v9h8V12" fill="none" stroke="#1a8fd8" stroke-width="2.4" stroke-linejoin="round"/></svg>Home</div>
  <div class="nav-item"><svg width="32" height="32" viewBox="0 0 32 32"><rect x="3" y="5" width="26" height="24" rx="2" fill="none" stroke="#8b8b8b" stroke-width="2.2"/><path d="M3 11h26M10 2v6M22 2v6M8 16h4M14 16h4M20 16h4M8 22h4M14 22h4M20 22h4" stroke="#8b8b8b" stroke-width="2"/></svg>Calendar</div>
  <div class="nav-item"><svg width="32" height="32" viewBox="0 0 32 32"><path d="M4 15V4h11l14 14-11 11z" fill="none" stroke="#8b8b8b" stroke-width="2.2" stroke-linejoin="round"/><circle cx="10" cy="10" r="2" fill="#8b8b8b"/></svg>Bookings</div>
  <div class="nav-item"><span class="nav-badge"><svg width="32" height="32" viewBox="0 0 32 32"><circle cx="16" cy="16" r="4.5" fill="none" stroke="#8b8b8b" stroke-width="2.2"/><path d="M14 3h4l1 4 3 1.5 3.5-2 3 3-2 3.5L28 16l-1 0 0 0 1 0v2l-4 1-1.5 3 2 3.5-3 3-3.5-2L15 29h-2l-1-4-3-1.5-3.5 2-3-3 2-3.5L3 16v-2l4-1 1.5-3-2-3.5 3-3 3.5 2L14 3z" fill="none" stroke="#8b8b8b" stroke-width="2" stroke-linejoin="round"/></svg></span>Settings</div>
</nav>
</body>
</html>
```